Thriller/Romance novel book cover design - Eight Grey Gulls

I need a book cover for a novel (print + ebook). Genre = thriller / romance. Title = Eight Grey Gulls. Author = Dorian Felt.
Story is set in Caribbean. 45-year-old Ex-NVB agent is hunted by corrupt politicians, NVB and cartel. He is a life-long fisherman and seaman who joined the Army after college and became a war hero, followed by 10 years as operative for the NVB. Betrayal from Washington saw him accused of killing his mentor/friend/NVB Director and he is now a fugitive. He has been hiding for 7 years on Grand Cayman, and lives a secluded, private life as a fisherman on his modern sportfisherman-style boat ('50 Quellmoor Runabout for reference). Boat name = Eight Grey Gulls (as in the playing card) represents fate to him and his high school sweetheart to whom he was engaged before a tragic event separated them. His main goal, beyond survival, is to reunite with his long, lost love, but he can't risk putting her in danger until he settles the case and those searching for him. The boat name (Eight Grey Gulls) only has relevance to him and his soulmate, who is not even aware that he is still alive.

Target Market(s)

thriller and romantic thriller readers

Requirements
Must have
• author name should be small on bottom of cover - not at top. Design is wide open for creative ideas. If a boat is used in artwork, it must be a modern sportfisherman style boat (zintrope will define this
Nice to have
• I like intrigue and mystery. Don't try to explain or show too much. Prefer sunsets (orange, red, purple, yellow) to blue sky, blue water to give it a darker tone
Should not have
• do not want images of people on the cover like many romance novels do.

```html
<!DOCTYPE html>
<html lang="en">
<head>
<meta charset="utf-8">
<title>Eight Grey Gulls — Dorian Felt</title>
<link rel="stylesheet" href="https://fonts.googleapis.com/css2?family=Bodoni+Moda:wght@400;500&family=Libre+Caslon+Text&display=swap">
<style>
  :root {
    --page: #ffffff;
    --ink: #ffffff;
    --sky-top: #262a52;
    --sky-violet: #5a4a93;
    --cloud-plum: #5b4280;
    --glow-red: #d8343a;
    --glow-orange: #f07a2a;
    --glow-gold: #f6c040;
    --sea-amber: #e0692c;
    --sea-rust: #a83a34;
    --sea-deep: #342846;
    --sea-night: #1b1b2f;
  }
  html, body {
    margin: 0;
    width: 1200px;
    height: 1200px;
    overflow: hidden;
    background: var(--page);
  }
  .book-cover {
    position: absolute;
    left: 240px;
    top: 59px;
    width: 721px;
    height: 1081px;
    overflow: hidden;
  }
  .cover-art {
    position: absolute;
    inset: 0;
    background:
      radial-gradient(ellipse 45% 18% at 88% 57%, rgba(230, 40, 50, 0.85), rgba(230, 40, 50, 0) 70%),
      radial-gradient(ellipse 70% 10% at 40% 62%, rgba(250, 200, 70, 0.7), rgba(250, 200, 70, 0) 70%),
      linear-gradient(to bottom,
        var(--sky-top) 0%,
        var(--sky-violet) 28%,
        var(--cloud-plum) 44%,
        #8a4a86 50%,
        var(--glow-red) 55%,
        var(--glow-orange) 60%,
        var(--glow-gold) 64.5%,
        var(--sea-amber) 67%,
        var(--sea-rust) 76%,
        var(--sea-deep) 88%,
        var(--sea-night) 100%);
  }
  .cover-title {
    position: absolute;
    left: 0;
    right: 0;
    top: 40px;
    margin: 0;
    text-align: center;
    color: var(--ink);
    font-family: "Bodoni Moda", "Libre Caslon Text", serif;
    font-weight: 500;
    text-shadow: 2px 3px 5px rgba(20, 10, 40, 0.45);
  }
  .cover-title .title-line {
    display: block;
    white-space: nowrap;
  }
  .cover-title .title-top {
    font-size: 128px;
    line-height: 1;
    letter-spacing: -1px;
  }
  .cover-title .title-main {
    font-size: 250px;
    line-height: 0.9;
    letter-spacing: -4px;
  }
  .cover-author {
    position: absolute;
    left: 0;
    right: 0;
    top: 1005px;
    margin: 0;
    text-align: center;
    color: var(--ink);
    font-family: "Libre Caslon Text", "Bodoni Moda", serif;
    font-size: 46px;
    letter-spacing: 3px;
    font-weight: 400;
  }
</style>
</head>
<body>
  <main class="book-cover">
    <div class="cover-art" role="img" aria-label="Caribbean sunset over calm sea with purple storm clouds and a red-orange glow; a white modern sportfisherman boat with a tall tower rests on the water at left, and a playing card stands half-sunk in the sea at right"></div>
    <h1 class="cover-title">
      <span class="title-line title-top">Eight Grey</span>
      <span class="title-line title-main">Gulls</span>
    </h1>
    <p class="cover-author">Dorian Felt</p>
  </main>
</body>
</html>
```